Holloway Photography.
I really don't know what should go here
Simple
Glen Holloway
Owner
4820 NE Corvel Dr Brennick Ia 50990
holloway.photography@brevanmail.com
hollowayphotography.net
I am thinking that i will put a photo, or just my logo on one side, and the rest of the info on the other.
This is one of those moments...
let us tell your story.

```html
<!DOCTYPE html>
<html lang="en">
<head>
<meta charset="utf-8">
<title>Holloway Photography – Business Card</title>
<link rel="stylesheet" href="https://fonts.googleapis.com/css2?family=Cinzel:wght@400&family=Open+Sans:wght@400;600&display=swap">
<style>
  :root {
    --stage: #e9e7e4;
    --card-light: #ffffff;
    --card-light-edge: #e4e4e4;
    --ink: #1b1b1b;
    --ink-soft: #4a4a4a;
    --band: #111111;
    --band-grey: #8c8c8c;
    --card-dark: #2a2a2a;
    --card-dark-deep: #121212;
    --on-dark: #f2f2f2;
    --rule-dark: #9a9a9a;
  }
  * { box-sizing: border-box; margin: 0; padding: 0; }
  html, body { width: 1200px; height: 456px; overflow: hidden; }
  body { background: var(--stage); position: relative; font-family: "Open Sans", Arial, sans-serif; }

  .card {
    position: absolute; top: 84px; width: 470px; height: 290px;
    box-shadow: 0 4px 14px rgba(0,0,0,.25);
    overflow: hidden;
  }

  /* Front: contact side */
  .card-front {
    left: 125px;
    background: linear-gradient(100deg, var(--card-light) 40%, var(--card-light-edge) 100%);
  }
  .front-stripes { position: absolute; left: 0; top: 0; }
  .brand-front {
    position: absolute; left: 85px; top: 40px; width: 190px;
    display: flex; flex-direction: column; align-items: center; gap: 10px;
  }
  .brand-mark { width: 44px; height: 44px; border-radius: 50%; background: var(--ink); }
  .brand-name {
    font-family: "Cinzel", Georgia, serif; font-size: 14px; color: var(--ink);
    letter-spacing: .4px; white-space: nowrap;
  }
  .address {
    position: absolute; left: 36px; top: 164px;
    font-size: 9.5px; line-height: 13px; color: var(--ink);
  }
  .contact-list {
    position: absolute; left: 36px; top: 208px; list-style: none;
    font-size: 9.5px; line-height: 16px; color: var(--ink);
  }
  .contact-list .label { display: inline-block; width: 14px; font-weight: 600; }
  .owner { position: absolute; left: 300px; top: 162px; }
  .owner-name {
    font-family: "Cinzel", Georgia, serif; font-size: 16px; color: var(--ink); white-space: nowrap;
  }
  .owner-title { font-size: 9px; color: var(--ink-soft); margin-top: 1px; }

  /* Back: image side */
  .card-back {
    left: 605px;
    background: radial-gradient(ellipse at 40% 40%, var(--card-dark) 0%, var(--card-dark-deep) 100%);
  }
  .back-photo {
    position: absolute; inset: 0;
    background: radial-gradient(ellipse 180px 120px at 170px 140px, rgba(110,110,110,.55), rgba(90,90,90,0) 100%);
  }
  .brand-back {
    position: absolute; left: 0; right: 0; top: 48px;
    display: flex; flex-direction: column; align-items: center; gap: 12px;
  }
  .brand-back .brand-mark { width: 54px; height: 54px; background: var(--on-dark); }
  .brand-back .brand-name { color: var(--on-dark); font-size: 15px; }
  .back-url {
    position: absolute; left: 0; right: 0; top: 232px; text-align: center;
    font-size: 9px; color: var(--on-dark); letter-spacing: .3px;
  }
  .back-rule { position: absolute; left: 0; right: 0; height: 1px; background: var(--rule-dark); }
  .back-rule.upper { top: 228px; }
  .back-rule.lower { top: 250px; }
</style>
</head>
<body>
  <section class="card card-front" aria-label="Business card front">
    <svg class="front-stripes" width="80" height="290" viewBox="0 0 80 290" aria-hidden="true">
      <rect x="0" y="0" width="24" height="290" fill="var(--band-grey)" opacity=".35"/>
      <rect x="0" y="0" width="24" height="62" fill="var(--band)"/>
      <rect x="0" y="12" width="74" height="7" fill="var(--band)"/>
      <rect x="0" y="28" width="74" height="7" fill="var(--band)"/>
      <rect x="0" y="44" width="74" height="7" fill="var(--band)"/>
    </svg>

    <div class="brand-front">
      <span class="brand-mark" aria-hidden="true"></span>
      <span class="brand-name">Holloway Photography.</span>
    </div>

    <p class="address">4820 NE Corvel Dr Brennick<br>Ia 50990</p>
    <ul class="contact-list">
      <li><span class="label">P</span>: 555-555-0142</li>
      <li><span class="label">E</span>: holloway.photography@brevanmail.com</li>
      <li><span class="label">W</span>: www.hollowayphotography.net</li>
    </ul>

    <div class="owner">
      <p class="owner-name">Glen Holloway</p>
      <p class="owner-title">Managing Director</p>
    </div>
  </section>

  <section class="card card-back" aria-label="Business card back">
    <div class="back-photo" role="img" aria-label="Dark, softly lit black-and-white photograph of a couple"></div>
    <div class="brand-back">
      <span class="brand-mark" aria-hidden="true"></span>
      <span class="brand-name">Holloway Photography.</span>
    </div>
    <span class="back-rule upper"></span>
    <p class="back-url">www.hollowayphotography.net</p>
    <span class="back-rule lower"></span>
  </section>
</body>
</html>
```